Red Fern Media Outdoor Advertising Corporate Stationery Design

We need a full corporate stationary design for our company Red Fern Media. We setup and lease billboards, building wraps, trailer ads and construction hoardings.

We need to establish our branding and our newly created logo. All our brand identity should point towards our values, vision and mission.

We are open to fresh new ideas for our stationary design as long as it ultimately reflects the brand & logo.

Corporate Stationary List:
1. Business Card Design
2. Letterhead Design
3. Email Signature Design
4. “Advertise Here” Design (for placement on empty billboards, etc)

All designs must include our logo and be kept simple, modern, friendly and effective.

All designs should please be provided in Illustrator, Photoshop and InDesign file formats.

More details are attached in Word.

Hey

The project has been guaranteed. We like what has been submitted so far but we''d like to see a few concepts for the "Advertise Here" design for open billboards please.

Thanks!

Target Market(s)

Male and female, corporates, business owners, media buying agencies, government & all age groups.

Industry/Entity Type

Construction

Requirements
Must have
• All designs must incorporate our colours: Pantone 319C, 320C, 321C & Hexachrome Black C.

1.Business Card Design
a. Logo
b. Name
c. Mobile
d. Landline
e. Website
f. Facebook
g. Twitter
2. Letterhead Design
a. Logo
b. Mobile
c. Landline
d. Website
e. CC reg number
f. BEE level 4 contributor
g. PRAVU member
h. Postal Address
3. Email Signature Design
a. Logo
b. Name
c. Mobile
d. Landline
e. BEE level 4 contributor
f. PRAVU member
g. Website
h. Facebook
i. Twitter
4. “Advertise Here” Design (for placement on empty billboards, etc) Majority ratio of 2:1 (eg 6m wide by 3m high) - Please use 2 attached photos.
a. Logo .co.za
b. Contact Nadia
c. Mobile
Nice to have
• Come up with a cool slogan / tagline for Business Cards, “Advertise Here” Design

```html
<!DOCTYPE html>
<html lang="en">
<head>
<meta charset="utf-8">
<title>Red Fern Media – Business Card</title>
<link href="https://fonts.googleapis.com/css2?family=Open+Sans:wght@400;600;700;800&display=swap" rel="stylesheet">
<style>
  :root {
    --teal-dark: #008b99;
    --teal-mid: #0aa3b0;
    --teal-light: #6ccad3;
    --ink: #1a1a1a;
    --grey: #555555;
    --paper: #ffffff;
    --backdrop: #eeeeec;
    --edge: #6b6b6b;
  }
  * { box-sizing: border-box; margin: 0; padding: 0; }
  html, body { width: 1200px; height: 428px; overflow: hidden; }
  body {
    background: var(--backdrop);
    font-family: "Open Sans", Arial, sans-serif;
    position: relative;
  }
  .card {
    position: absolute;
    background: var(--paper);
    border: 1px solid var(--edge);
  }
  .card-front { left: 65px; top: 65px; width: 268px; height: 297px; }
  .card-divider { position: absolute; left: 334px; top: 65px; width: 3px; height: 297px; background: #2c3e44; }
  .card-back {
    left: 338px; top: 65px; width: 248px; height: 297px;
    background: var(--teal-dark); border: none; color: var(--paper);
  }
  .card-wide { left: 622px; top: 67px; width: 520px; height: 297px; }

  .brand {
    position: absolute; display: flex; align-items: center; gap: 8px;
    font-weight: 800; color: var(--ink); white-space: nowrap;
  }
  .brand-mark { background: var(--teal-dark); flex: none; }
  .card-front .brand { left: 40px; top: 160px; font-size: 22px; }
  .card-front .brand-mark { width: 16px; height: 16px; }
  .card-wide .brand { left: 50%; transform: translateX(-50%); top: 170px; font-size: 44px; gap: 14px; }
  .card-wide .brand-mark { width: 32px; height: 32px; }

  .tagline {
    position: absolute; left: 0; right: 0; top: 203px; text-align: center;
    font-weight: 700; font-size: 15px; letter-spacing: 2px; color: var(--grey);
  }

  .holder { position: absolute; left: 28px; top: 86px; font-size: 16px; font-weight: 700; }
  .holder .role { font-size: 12px; font-weight: 400; }
  .contact-list { position: absolute; left: 28px; top: 129px; list-style: none; font-size: 12.5px; line-height: 18px; }
  .contact-list li { display: flex; align-items: center; gap: 5px; }
  .contact-list svg { width: 9px; height: 9px; flex: none; }

  .site {
    position: absolute; left: 0; right: 0; top: 262px; text-align: center;
    font-size: 12.5px; letter-spacing: 2.6px; color: #444;
  }
</style>
</head>
<body>
  <section class="card card-front">
    <div class="brand"><span class="brand-mark"></span>Red Fern Media</div>
    <p class="tagline">Advertise Here</p>
  </section>
  <div class="card-divider"></div>
  <section class="card card-back">
    <p class="holder">Your Name / <span class="role">Title</span></p>
    <ul class="contact-list">
      <li><svg viewBox="0 0 10 10"><path d="M2 1 L4 1 L4.5 3 L3.3 4 Q4.5 6 6 6.7 L7 5.5 L9 6 L9 8 Q8 9 6 8.5 Q2 7 1 3 Q1 1.5 2 1Z" fill="#fff"/></svg>+91 12345 67890</li>
      <li><svg viewBox="0 0 10 10"><rect x="2.5" y="0.5" width="5" height="9" rx="1" fill="none" stroke="#fff"/><rect x="3.5" y="2" width="3" height="4" fill="#fff"/></svg>+91 12345 67890</li>
      <li><svg viewBox="0 0 10 10"><circle cx="5" cy="5" r="4.2" fill="none" stroke="#fff"/><ellipse cx="5" cy="5" rx="1.8" ry="4.2" fill="none" stroke="#fff" stroke-width="0.8"/><line x1="0.8" y1="5" x2="9.2" y2="5" stroke="#fff" stroke-width="0.8"/></svg>www.redfernmedia.com</li>
      <li><svg viewBox="0 0 10 10"><rect x="1" y="1" width="8" height="8" fill="#dfe8f2"/></svg>redfernmedia.com</li>
      <li><svg viewBox="0 0 10 10"><rect x="1" y="1" width="8" height="8" fill="#cfeef6"/></svg>redfernmedia.com</li>
    </ul>
  </section>
  <section class="card card-wide">
    <div class="brand"><span class="brand-mark"></span>Red Fern Media</div>
    <p class="site">www.redfernmedia.com</p>
  </section>
</body>
</html>
```